Commercial Bakery needs packing design for a Bread Bag.

Dorne's Bakery needs a design for a bread bag to be distributed to grocery stores. We make all kinds of breads and want this packaging to represent our company. We would like the packaging to be black and white with a fun/bubbly modern design. I have attached a few ideas of what I am looking for.
There are 5 different products. Packaging must be the same for each product except for corresponding product name, bar code and nutrional facts.
Product names:
Coconut Cream Bread
Cream Bread
Potato Rolls
Roll ups
Coconut & Raisin Bread

Our products are packaged in a 11” x 8” poly bag.
I will open 5 contracts with whoever’s design I select. I will then provide nutritional facts, barcodes for items once a contract is selected. Thank you!!

Target Market(s)

Grocery stores

Industry/Entity Type

Bakery

Requirements
Must have
• Black and White (off whites are ok)
Should not have
• Color

```html
<!DOCTYPE html>
<html lang="en">
<head>
<meta charset="utf-8">
<title>Dorne's Bakery – Potato Rolls</title>
<link rel="stylesheet" href="https://fonts.googleapis.com/css2?family=Fredoka:wght@600&family=Lexend:wght@400;600&display=swap">
<style>
  :root {
    --ink: #000000;
    --paper: #ffffff;
  }
  * { margin: 0; padding: 0; box-sizing: border-box; }
  html, body {
    width: 901px;
    height: 1200px;
    overflow: hidden;
    background: var(--paper);
  }
  .bag-front {
    position: relative;
    width: 901px;
    height: 1200px;
    background: var(--paper);
    color: var(--ink);
  }
  .brand {
    position: absolute;
    left: 100px;
    top: 70px;
    width: 701px;
    height: 690px;
    display: flex;
    align-items: center;
    justify-content: center;
    text-align: center;
  }
  .brand-name {
    font-family: "Lexend", sans-serif;
    font-weight: 600;
    font-size: 128px;
    line-height: 1.05;
    letter-spacing: -1px;
    color: var(--ink);
  }
  .product-name {
    position: absolute;
    left: 78px;
    top: 848px;
    font-family: "Fredoka", sans-serif;
    font-weight: 600;
    font-size: 100px;
    line-height: 95px;
    letter-spacing: 1px;
    color: var(--ink);
  }
  .divider {
    position: absolute;
    left: 473px;
    top: 821px;
    width: 7px;
    height: 283px;
    background: var(--ink);
  }
  .ingredients {
    position: absolute;
    left: 499px;
    top: 868px;
    width: 300px;
    color: var(--ink);
  }
  .ingredients-title {
    font-family: "Lexend", sans-serif;
    font-weight: 600;
    font-size: 35px;
    line-height: 40px;
    letter-spacing: 0.3px;
  }
  .ingredients-list {
    margin-top: 10px;
    padding-left: 8px;
    font-family: "Lexend", sans-serif;
    font-weight: 400;
    font-size: 16.5px;
    line-height: 22.5px;
    white-space: nowrap;
  }
</style>
</head>
<body>
  <main class="bag-front">
    <header class="brand">
      <p class="brand-name">Dorne's<br>Bakery</p>
    </header>

    <h1 class="product-name">POTATO<br>ROLLS</h1>

    <div class="divider"></div>

    <section class="ingredients">
      <h2 class="ingredients-title">INGREDIENTS</h2>
      <p class="ingredients-list">Wheat Flour (Wheat flour,<br>Thiamin, Niacin, Calcium<br>Carbonate, Iron), Water,<br>Salt, Soya Flour, Yeast,<br>Preservatives: Calcium<br>Propionate, Acetic Acid;</p>
    </section>
  </main>
</body>
</html>
```